Postcard needed for expert witness service

Looking for a professional postcard that will be mailed to personal injury lawyers / law firms to introduce my expert witness services.

Target Market(s)

Law firms, personal injury lawyers

Industry/Entity Type

Expert witness, law

Font styles to use
Sans Serif

Requirements
Must have
• Logo: The Frost Counsel [Main Heading]Do you handle snow and ice related slip and falls? Darrel is one of the top snow industry experts in the country! [Following should be in a list type fashion, possibly bulleted]Darrel's credentials: Accredited Winter Practitioner (AWP), past WRTA board member and chair, former ISO 9001 certified snow company owner , 32 years in the industry. (555) 284-3917 NOTES: Postcard will be 4" x 6" Please use both sides however must have room for labels and stamp
Should not have
• Wouldn't suggest using both photos on same side. Honestly, feel free to only use one of the slip and fall photos if it works out better. Thanks!

```html
<!DOCTYPE html>
<html lang="en">
<head>
<meta charset="utf-8">
<title>The Frost Counsel — Postcard</title>
<link rel="stylesheet" href="https://fonts.googleapis.com/css2?family=Oswald:wght@400;500;600&display=swap">
<style>
  :root {
    --backdrop: #9b9b9b;
    --ink: #000000;
    --paper: #ffffff;
    --rule: #6b6b6b;
    --photo-light: #d9d6d2;
    --photo-mid: #8f8a84;
    --photo-dark: #4a3f3a;
  }
  html, body {
    margin: 0;
    padding: 0;
    width: 1151px;
    height: 1200px;
    overflow: hidden;
    background: var(--backdrop);
  }
  .postcard {
    position: absolute;
    left: 259px;
    width: 633px;
    height: 422px;
    display: block;
  }
  .postcard--front { top: 96px; }
  .postcard--back { top: 647px; }
  .headline { font-family: "Oswald", sans-serif; font-weight: 600; }
  .claim { font-family: "Oswald", sans-serif; font-weight: 500; }
  .credential { font-family: "Oswald", sans-serif; font-weight: 400; }
  .phone-number { font-family: "Oswald", sans-serif; font-weight: 500; }
  .brand-name { font-family: "Oswald", sans-serif; font-weight: 500; }
</style>
</head>
<body>

<svg class="postcard postcard--front" viewBox="0 0 1034 689" xmlns="http://www.w3.org/2000/svg">
  <defs>
    <linearGradient id="photo-tone" x1="0" y1="0" x2="1" y2="1">
      <stop offset="0" stop-color="var(--photo-mid)"/>
      <stop offset="0.5" stop-color="var(--photo-dark)"/>
      <stop offset="1" stop-color="var(--photo-light)"/>
    </linearGradient>
    <symbol id="phone-icon" viewBox="0 0 42 42">
      <path fill="currentColor" d="M8 5C5 5 3 8 4 12C7 25 18 35 31 38C35 39 38 37 38 34L38 29L30 25L26 29C20 27 15 22 13 16L17 12L13 5Z"/>
      <path fill="none" stroke="currentColor" stroke-width="2.5" stroke-linecap="round" d="M23 13A7 7 0 0 1 29 19M24 7A13 13 0 0 1 35 18M25 1A19 19 0 0 1 41 17"/>
    </symbol>
  </defs>

  <rect class="card-paper" width="1034" height="689" fill="var(--paper)"/>

  <path class="hero-photo" role="img" aria-label="Photo of a woman in a winter coat and knit hat who has slipped and fallen on an icy path"
        d="M478 0L1034 0L1034 689L757 689C510 560 370 290 478 0Z" fill="url(#photo-tone)"/>

  <path class="accent-arc" d="M422 0L458 0C380 160 365 420 577 640L548 640C330 430 345 170 422 0Z" fill="var(--ink)"/>
  <path class="claim-band" d="M0 415L386 415C425 520 490 590 577 640L0 640Z" fill="var(--ink)"/>

  <rect class="phone-bar" x="514" y="467" width="520" height="86" fill="var(--ink)"/>
  <use href="#phone-icon" x="600" y="485" width="52" height="52" color="var(--paper)"/>
  <text class="phone-number" x="674" y="529" font-size="46" fill="var(--paper)" textLength="238" lengthAdjust="spacingAndGlyphs">(555) 284-3917</text>

  <text class="brand-name" x="197" y="120" font-size="40" fill="var(--ink)" text-anchor="middle" textLength="290" lengthAdjust="spacingAndGlyphs">THE FROST COUNSEL</text>

  <g class="headline" fill="var(--ink)" text-anchor="middle">
    <text x="196" y="263" font-size="62" textLength="296" lengthAdjust="spacingAndGlyphs">DO YOU HANDLE</text>
    <text x="196" y="315" font-size="40" textLength="298" lengthAdjust="spacingAndGlyphs">SNOW AND ICE RELATED</text>
    <text x="196" y="373" font-size="56" textLength="300" lengthAdjust="spacingAndGlyphs">SLIP AND FALLS?</text>
  </g>

  <g class="claim" fill="var(--paper)" text-anchor="middle">
    <text x="215" y="488" font-size="40" textLength="345" lengthAdjust="spacingAndGlyphs">DARREL IS ONE OF THE TOP</text>
    <text x="215" y="541" font-size="40" textLength="347" lengthAdjust="spacingAndGlyphs">SNOW INDUSTRY EXPERTS</text>
    <text x="215" y="608" font-size="66" textLength="345" lengthAdjust="spacingAndGlyphs">IN THE COUNTRY!</text>
  </g>
</svg>

<svg class="postcard postcard--back" viewBox="0 0 1034 689" xmlns="http://www.w3.org/2000/svg">
  <defs>
    <symbol id="phone-icon-back" viewBox="0 0 42 42">
      <path fill="currentColor" d="M8 5C5 5 3 8 4 12C7 25 18 35 31 38C35 39 38 37 38 34L38 29L30 25L26 29C20 27 15 22 13 16L17 12L13 5Z"/>
      <path fill="none" stroke="currentColor" stroke-width="2.5" stroke-linecap="round" d="M23 13A7 7 0 0 1 29 19M24 7A13 13 0 0 1 35 18M25 1A19 19 0 0 1 41 17"/>
    </symbol>
  </defs>

  <rect class="card-paper" width="1034" height="689" fill="var(--paper)"/>

  <path class="credentials-panel" d="M0 0L432 0C560 170 575 350 500 502L0 502Z" fill="var(--ink)"/>
  <path class="accent-arc" d="M478 0L515 0C625 190 612 460 405 689L383 689C582 460 592 210 478 0Z" fill="var(--ink)"/>
  <path class="footer-band" d="M0 590L455 590C425 625 395 660 370 689L0 689Z" fill="var(--ink)"/>

  <text class="headline" x="57" y="188" font-size="50" fill="var(--paper)" textLength="362" lengthAdjust="spacingAndGlyphs">DARREL'S CREDENTIALS:</text>

  <g class="credential-list" fill="var(--paper)">
    <circle cx="62" cy="243" r="5"/>
    <text class="credential" x="88" y="253" font-size="28" textLength="310" lengthAdjust="spacingAndGlyphs">Accredited Winter Practitioner (AWP)</text>
    <circle cx="62" cy="308" r="5"/>
    <text class="credential" x="84" y="318" font-size="28" textLength="316" lengthAdjust="spacingAndGlyphs">past WRTA board member and chair</text>
    <circle cx="62" cy="374" r="5"/>
    <text class="credential" x="84" y="384" font-size="28" textLength="426" lengthAdjust="spacingAndGlyphs">former ISO 9001 certified snow company owner</text>
    <circle cx="62" cy="439" r="5"/>
    <text class="credential" x="84" y="449" font-size="28" textLength="216" lengthAdjust="spacingAndGlyphs">32 years in the industry</text>
  </g>

  <use href="#phone-icon-back" x="74" y="520" width="52" height="52" color="var(--ink)"/>
  <text class="phone-number" x="149" y="565" font-size="46" fill="var(--ink)" textLength="238" lengthAdjust="spacingAndGlyphs">(555) 284-3917</text>

  <rect class="stamp-box" x="807" y="56" width="136" height="135" fill="none" stroke="var(--rule)" stroke-width="3"/>

  <g class="address-lines" stroke="var(--rule)" stroke-width="2">
    <line x1="623" y1="284" x2="959" y2="284"/>
    <line x1="623" y1="340" x2="959" y2="340"/>
    <line x1="623" y1="395" x2="959" y2="395"/>
  </g>

  <text class="brand-name" x="792" y="575" font-size="40" fill="var(--ink)" text-anchor="middle" textLength="306" lengthAdjust="spacingAndGlyphs">THE FROST COUNSEL</text>
</svg>

</body>
</html>
```